Heaven, guard me from choosing Korith

I need a book cover to be designed for a book I am writing about marrying the wrong man. I need the cover to be very eye-catching with an emotional, sympathetic and compassionate feel. Gold can be used along with any other colours . I want a very feminine feel to the book cover. I don't mind a cartoon design but must be elegant,
Let me give you a hint about Korith, he is a very wealthy man, good looking a narcissist, a high flyer jet-setter, very very mean with his money. Really know how to pull the girls but treat them badly, he is the kind of man any women would fall for. With this information create me a cover that when any women look at they can identify and will buy the book.
Target Market(s)
Female, single women, divorced women, women who are dating.
Colors
Designer to choose colors to be used in the design.
Requirements
Must have
- must have some kind of picture o to it, bold writing of the book title yet soft in appearance. Elegant, sophisticated and very expensive yet attractive. Modern in appearance very much 21st century look to it. please stay away from the church, wedding dress.
Nice to have
- Nice to have a playful cover, yet very elegant and modern.
Should not have
- The design of the book cover should not have, any church wedding dress graphics. The book size is a jpg at 300 dpi with A5 dimensions (14.8 cm wide by 21 cm high), and make sure that your text is well within the trim line - approximately 2 cm from the edge.
- This is my autobiography
- This book aims to teach you informative Guide and strategies, how to attract the right kind of man to be your husband. What you also learn is how to understand the social fundamental truth sharps the relationship the man will have with himself and the rest of the world.
- This book will uncover the 10 worst men to Marry, using the biblical character to name these bad boys, you will learn that in today's 21st century these character is still very much around.
- Things you will learn from reading this book.
- .Break the cycle of the failed relationship.
- .Understanding the fundamental truth about a man life.
- . Recognize red flags you should not ignore when dating.
- .Strategies on how to win the spiritual on singleness
- . The do's and don't of dating.
- .How to equip yourself to defeat the curse anti-marriage
- Dovella Brannick is co-leader with her husband Marcus Brannick Beacon 700 prayer ministry in London, England where they live with their three grown children and Ethan their energetic 13yrs old superstar. The ministry is renowned for their Deliverance services and Teaching where Dovella teaches the word of God with deep spiritual insight. She also has a prophetic insight into dreams and vision from a biblical perspective. Beacon 700 prayer ministry is a 24 hours prayer warriors group who observe the 8 prayer watches. The ministry is known for their powerful teaching seminar as well there 72 prayer hours shut-in service,as well as their mentorship programme and master classes on singleness and marriages.
- please put the picture of my self on the back. I have uploaded

```html
<!DOCTYPE html>
<html lang="en">
<head>
<meta charset="utf-8">
<title>Heaven, Guard Me From Choosing Korith — Book Cover</title>
<link rel="stylesheet" href="https://fonts.googleapis.com/css2?family=Jost:ital,wght@0,400;0,500;0,600;0,800;0,900;1,400&family=Bowlby+One&display=swap">
<style>
  :root {
    --cover-red: #e0100d;
    --cover-red-deep: #c40b08;
    --paper: #f6f5f2;
    --paper-edge: #e2e0dc;
    --ink: #0b0b0b;
    --photo-dark: #2a2a2a;
    --photo-mid: #7a7a7a;
    --photo-light: #cfcfcf;
  }
  * { margin: 0; padding: 0; box-sizing: border-box; }
  html, body { width: 838px; height: 1200px; overflow: hidden; background: var(--paper); }
  .cover {
    position: relative;
    width: 838px;
    height: 1200px;
    overflow: hidden;
    background: var(--paper);
    font-family: "Jost", sans-serif;
  }
  .cover-art { position: absolute; inset: 0; width: 838px; height: 1200px; }
  .title-block {
    position: absolute;
    top: 118px; left: 0; width: 100%;
    text-align: center;
    color: var(--ink);
  }
  .title-lead {
    font-style: italic;
    font-weight: 400;
    font-size: 62px;
    line-height: 1;
    letter-spacing: 1px;
  }
  .title-sub {
    margin-top: 10px;
    font-style: italic;
    font-weight: 400;
    font-size: 45px;
    line-height: 1;
    letter-spacing: 2px;
  }
  .title-main {
    margin-top: 8px;
    font-weight: 900;
    font-size: 118px;
    line-height: 1;
    letter-spacing: 1px;
  }
  .tagline {
    position: absolute;
    top: 860px; left: 0; width: 100%;
    text-align: center;
    font-family: "Bowlby One", sans-serif;
    font-size: 34px;
    letter-spacing: 1px;
    color: var(--cover-red);
    -webkit-text-stroke: 1.5px var(--ink);
  }
  .highlights {
    position: absolute;
    top: 924px; left: 0; width: 100%;
    list-style: none;
    text-align: center;
    color: var(--cover-red-deep);
    font-size: 18.5px;
    line-height: 26px;
    letter-spacing: 0.3px;
  }
  .highlights li::before { content: "\2022\00a0"; }
  .author {
    position: absolute;
    top: 1100px; left: 0; width: 100%;
    text-align: center;
    font-weight: 600;
    font-size: 54px;
    letter-spacing: 3px;
    color: var(--ink);
  }
</style>
</head>
<body>
<main class="cover">
  <svg class="cover-art" viewBox="0 0 838 1200" aria-hidden="true">
    <defs>
      <linearGradient id="suit-tones" x1="0" y1="0" x2="1" y2="1">
        <stop offset="0" stop-color="var(--photo-light)"/>
        <stop offset="0.35" stop-color="var(--photo-mid)"/>
        <stop offset="0.7" stop-color="var(--photo-dark)"/>
        <stop offset="1" stop-color="#3c3c3c"/>
      </linearGradient>
    </defs>
    <!-- red bands -->
    <rect class="band-top" x="0" y="0" width="838" height="130" fill="var(--cover-red)"/>
    <rect class="band-bottom" x="0" y="1050" width="838" height="150" fill="var(--cover-red)"/>
    <!-- torn paper panel holding the title -->
    <path class="paper-title" fill="var(--paper)" stroke="var(--paper-edge)" stroke-width="2"
      d="M0 112 L40 110 L85 113 L130 109 L180 112 L230 110 L290 113 L350 109 L410 112 L470 110 L530 113 L590 109 L650 112 L710 110 L770 113 L838 110
         L838 393 L790 395 L740 392 L690 396 L640 393 L590 396 L540 392 L490 395 L440 393 L390 396 L340 392 L290 395 L240 393 L190 396 L140 392 L90 395 L40 393 L0 395 Z"/>
  </svg>

  <svg class="cover-art" viewBox="0 0 838 1200" role="img" aria-label="Black and white photo of a man in a dark suit fastening his shirt cuff link">
    <path fill="url(#suit-tones)"
      d="M0 396 L40 394 L90 396 L140 393 L190 397 L240 394 L290 396 L340 393 L390 397 L440 394 L490 396 L540 393 L590 397 L640 394 L690 396 L740 393 L790 396 L838 394
         L838 742 L810 748 L780 740 L750 752 L720 746 L690 760 L660 754 L630 768 L600 762 L570 776 L540 772 L510 784 L480 778 L450 790 L420 786 L390 796 L360 790 L330 800 L300 794 L270 804 L240 798 L210 808 L180 800 L150 810 L120 802 L90 808 L60 800 L30 806 L0 798 Z"/>
  </svg>

  <svg class="cover-art" viewBox="0 0 838 1200" aria-hidden="true">
    <!-- torn lower edge into red band -->
    <path class="paper-edge-bottom" fill="var(--paper)" stroke="var(--paper-edge)" stroke-width="2"
      d="M0 1060 L50 1064 L100 1061 L150 1065 L200 1062 L250 1066 L300 1062 L350 1065 L400 1061 L450 1065 L500 1062 L550 1066 L600 1062 L650 1065 L700 1061 L750 1065 L800 1062 L838 1064 L838 1040 L0 1040 Z"/>
  </svg>

  <header class="title-block">
    <h1>
      <span class="title-lead" style="display:block">HEAVEN,</span>
      <span class="title-sub" style="display:block">GUARD ME FROM CHOOSING</span>
      <span class="title-main" style="display:block">KORITH</span>
    </h1>
  </header>

  <p class="tagline">THE DO'S AND DON'TS OF DATING</p>

  <ul class="highlights">
    <li>10 Worst Men You Can Marry</li>
    <li>Understanding the Fundamental Truth about a man's life</li>
    <li>Red flags you should NOT ignore when dating</li>
    <li>Informative guides to help you attract your perfect husband</li>
  </ul>

  <p class="author">DOVELLA BRANNICK</p>
</main>
</body>
</html>
```